TerraLume Business Card Design Project

We need a business card design for a new company called "TerraLume Systems". TerraLume provides 3D visualization software for subsurface oil and gas data so you can make confident downhole decisions.

Our goal is to provide easy to understand big pictures of your data so your can make confident planning decisions.

Our tagline is
SEAMLESS DATA SHARING. EFFECTIVE COLLABORATION. CONFIDENT DECISION-MAKING

Check out http://www.terralume-example.com for more ideas.

The design should promote a technology company that delivers web-based solutions focused on photo-realistic 3D graphics.

The colors from our existing logo (attached) are one option but not a requirement. The design SHOULD NOT use the existing logo.

The design should be two sided and full color. If you require any special print considerations (example: paper type, matte finish, metallic ink, etc) please provide detailed comments. Please also specify any desired details such as rounding of corners, etc.

IF YOU USE BLACK our printer states "We recommend using CMYK black (0, 0, 0, 100) or for a rich black (60, 40, 40, 100). Ensure your artwork is in CMYK mode before adjusting the black."

For design purposes you can use the following contact information

name: Harlan Pike
title: founder
phone: 555.987.6543
email: harlan@terralume-example.com

company information
TerraLume is our "branded" name
"TerraLume Systems" is our official name
www.terralume-example.com

address:
Suite 720
482 Birchmont Avenue SW
Calgary, AB, Canada
T3K 4R8

Target Market(s)

Companies spend a lot of time collecting, organizing and analyzing data but it's really hard to to get a big picture view of current and planned projects, especially in context to existing wellbores, geology and downhole equipment

TerraLume enables you to explore the big picture in an immersive, 3D environment. Our goal is to help transform you rich data into an easily understood picture, to make confident planning decisions and anticipate trouble events before the expensive execution phase.

Industry/Entity Type

Oil And Gas

Requirements
Must have
• The business card design should be sized to a standard 3.5 x 2 inches and print ready. See the attachment for a sample sized card
It MUST meet these requirements:
Exported as PDF file with two pages:
page 1: front design
page 2: back design
All Images must be 300ppi or higher (at 100%)
CMYK colour mode
0.125 inches of bleed on all sides (0.25 inches additional width and height)
0.125 inch safety margin (inside trim line)

```html
<!DOCTYPE html>
<html lang="en">
<head>
<meta charset="utf-8">
<title>TerraLume Systems – Business Card Front</title>
<link rel="stylesheet" href="https://fonts.googleapis.com/css2?family=Source+Sans+3:wght@400;700&display=swap">
<style>
  :root {
    --paper: #ffffff;
    --ink: #111111;
    --brand-green: #4cff00;
    --green-pale: #e9ffd9;
    --green-mid: #a8ff7a;
    --charcoal: #111111;
    --slate: #5a5a5a;
    --edge-light: #d8d8d8;
    --edge-dark: #222222;
    --crop: #000000;
  }
  html, body {
    margin: 0;
    padding: 0;
    width: 1200px;
    height: 759px;
    overflow: hidden;
    background: var(--paper);
  }
  .card {
    display: block;
    width: 1200px;
    height: 759px;
  }
  .crop-mark { stroke: var(--crop); stroke-width: 1; }
  .wordmark {
    font-family: "Source Sans 3", "Myriad Pro", sans-serif;
    font-weight: 700;
    font-size: 92px;
    fill: var(--brand-green);
  }
  .contact-text, .address-text {
    font-family: "Source Sans 3", "Myriad Pro", sans-serif;
    font-weight: 400;
    fill: var(--ink);
  }
  .contact-text { font-size: 28px; }
  .address-text { font-size: 29px; }
</style>
</head>
<body>
<svg class="card" viewBox="0 0 1225 777" xmlns="http://www.w3.org/2000/svg" role="img" aria-label="TerraLume Systems business card, front">
  <defs>
    <linearGradient id="swoosh-fill" x1="0" y1="0" x2="0" y2="1">
      <stop offset="0" style="stop-color:var(--charcoal)"/>
      <stop offset="1" style="stop-color:var(--slate)"/>
    </linearGradient>
    <linearGradient id="address-fill" x1="0" y1="0" x2="0" y2="1">
      <stop offset="0" style="stop-color:var(--green-pale)"/>
      <stop offset="0.6" style="stop-color:var(--brand-green)"/>
      <stop offset="1" style="stop-color:var(--brand-green)"/>
    </linearGradient>
    <linearGradient id="contact-fill" x1="0" y1="0" x2="1" y2="0">
      <stop offset="0.35" style="stop-color:var(--brand-green)"/>
      <stop offset="0.75" style="stop-color:var(--green-mid)"/>
      <stop offset="1" style="stop-color:var(--green-pale)"/>
    </linearGradient>
    <linearGradient id="edge-fill" x1="0" y1="0" x2="1" y2="0">
      <stop offset="0" style="stop-color:var(--edge-light)"/>
      <stop offset="1" style="stop-color:var(--edge-dark)"/>
    </linearGradient>
  </defs>

  <rect width="1225" height="777" fill="var(--paper)"/>

  <!-- trim marks -->
  <g class="crop-marks">
    <line class="crop-mark" x1="88" y1="0" x2="88" y2="62"/>
    <line class="crop-mark" x1="1138" y1="0" x2="1138" y2="62"/>
    <line class="crop-mark" x1="88" y1="712" x2="88" y2="777"/>
    <line class="crop-mark" x1="1138" y1="712" x2="1138" y2="777"/>
    <line class="crop-mark" x1="0" y1="88" x2="62" y2="88"/>
    <line class="crop-mark" x1="1162" y1="88" x2="1225" y2="88"/>
    <line class="crop-mark" x1="0" y1="688" x2="62" y2="688"/>
    <line class="crop-mark" x1="1162" y1="688" x2="1225" y2="688"/>
  </g>

  <!-- right edge rule and dark swoosh -->
  <line x1="1134" y1="74" x2="1134" y2="220" stroke="#cfcfcf" stroke-width="2"/>
  <path class="swoosh" d="M1135,212 C1125,470 930,640 590,681 L1135,681 Z" fill="url(#swoosh-fill)"/>

  <!-- wordmark -->
  <text class="wordmark" x="180" y="352">TerraLume</text>

  <!-- address panel -->
  <g class="address-panel">
    <path d="M700,350 L964,304 L1086,430 Q940,606 708,666 L578,533 Z" fill="url(#edge-fill)"/>
    <path d="M706,358 L960,314 L1076,434 Q932,598 712,656 L588,533 Z" fill="url(#address-fill)"/>
    <text class="address-text">
      <tspan x="698" y="417">Suite 720</tspan>
      <tspan x="698" y="458">482 Birchmont Avenue SW</tspan>
      <tspan x="698" y="498">Calgary, AB, Canada</tspan>
      <tspan x="698" y="538">T3K 4R8</tspan>
    </text>
  </g>

  <!-- contact panel -->
  <g class="contact-panel">
    <path d="M100,469 L346,469 L594,684 L104,684 Z" fill="url(#edge-fill)"/>
    <path d="M104,478 L342,478 L568,676 L104,676 Z" fill="url(#contact-fill)"/>
    <text class="contact-text">
      <tspan x="140" y="530">Harlan Pike</tspan>
      <tspan x="140" y="570">founder</tspan>
      <tspan x="140" y="610">555.987.6543</tspan>
      <tspan x="140" y="650">harlan@terralume-example.com</tspan>
    </text>
  </g>
</svg>
</body>
</html>
```